Brambleway Foundation Brochure

We are looking for a new brochure design for our foundation. The foundation is a nonprofit organization that provides assistance to special needs families in Indiana. We do this by providing ipads, communication software, gas cards, and financial assistance to families for their special needs child.

Target Market(s)

Families

Industry/Entity Type

Foundation

Colors
0355a3
3176b5
34a6d7
9bcb3b

Requirements
Must have
• Clear concise information

```html
<!DOCTYPE html>
<html lang="en">
<head>
<meta charset="utf-8">
<title>Brambleway Foundation Brochure</title>
<link rel="stylesheet" href="https://fonts.googleapis.com/css2?family=Open+Sans:ital,wght@0,400;0,600;0,700;1,700&family=Quattrocento:wght@400;700&display=swap">
<style>
:root{
  --navy:#0355a3;
  --blue:#3176b5;
  --sky:#34a6d7;
  --green:#9bcb3b;
  --ink:#5a5f66;
  --paper:#ffffff;
  --stage:#e4e6e8;
}
*{box-sizing:border-box;margin:0;padding:0}
html,body{width:1200px;height:800px;overflow:hidden;background:var(--stage);font-family:"Open Sans",sans-serif}
.sheet{position:absolute;top:182px;width:564px;height:436px;background:var(--paper);box-shadow:0 4px 14px rgba(0,0,0,.18);overflow:hidden}
.sheet--inside{left:24px}
.sheet--outside{left:612px}
.sheet-art{position:absolute;inset:0;width:564px;height:436px}
.fold{position:absolute;top:0;bottom:0;width:1px;background:rgba(0,0,0,.08)}
.block{position:absolute}
.heading-green{color:var(--green);font-weight:700;font-size:19px;line-height:1.05}
.body-copy{font-size:7.6px;line-height:1.42;color:var(--ink);text-align:justify}
.body-copy--light{color:#fff}
.web{font-size:8px;letter-spacing:4px;color:var(--green)}
.org-name{font-weight:700;color:var(--navy);font-size:12px;text-align:center;line-height:1.15;display:flex;flex-direction:column;align-items:center;gap:5px}
.org-name .dot{width:10px;height:10px;border-radius:50%;background:var(--green)}
.callout{color:#fff;font-weight:700;font-style:italic;font-size:12.5px;line-height:1.2}
.callout--big{font-size:19px;line-height:1.05}
.steps{list-style:none;font-size:7.2px;line-height:1.5;color:#fff}
.steps li::before{content:"\25CF";margin-right:4px;font-size:6px}
.difference-title{color:var(--navy);font-weight:700;font-style:italic;font-size:11px}
.difference-list{list-style:none;font-size:7.4px;line-height:1.6;color:#2d3a4a}
.difference-list li::before{content:"\25CF";color:var(--navy);margin-right:4px;font-size:6px}
.link{color:var(--green)}
.story-title{color:var(--green);font-weight:600;font-size:12px;text-align:center}
.signature{font-size:7.4px;color:#fff;text-align:right;line-height:1.35}
.signature strong{font-style:italic;font-weight:600;font-size:8.5px}
.contact{font-size:8px;color:#fff;text-align:right;line-height:1.45}
.contact hr{border:0;border-top:1px solid rgba(255,255,255,.6);margin:5px 0 5px 30px}
.tagline{font-family:"Quattrocento",serif;color:var(--green);font-size:26px;line-height:1.05}
.tagline span{display:block}
</style>
</head>
<body>

<section class="sheet sheet--inside" aria-label="Brochure inside spread">
  <svg class="sheet-art" viewBox="0 0 564 436">
    <defs>
      <linearGradient id="wave-blue" x1="0" y1="0" x2="1" y2="1">
        <stop offset="0" stop-color="#3176b5"/>
        <stop offset="1" stop-color="#0355a3"/>
      </linearGradient>
      <linearGradient id="photo-family" x1="0" y1="0" x2="1" y2="1">
        <stop offset="0" stop-color="#6b5144"/>
        <stop offset=".5" stop-color="#8a7a66"/>
        <stop offset="1" stop-color="#c25a8a"/>
      </linearGradient>
      <linearGradient id="photo-play" x1="0" y1="0" x2="1" y2="1">
        <stop offset="0" stop-color="#d7dcd6"/>
        <stop offset="1" stop-color="#b8c7cf"/>
      </linearGradient>
    </defs>
    <g role="img" aria-label="Photo of a mother holding her young daughter outdoors">
      <path d="M0,0 H188 V172 C150,190 110,205 60,210 C35,212 15,214 0,218 Z" fill="url(#photo-family)"/>
    </g>
    <g role="img" aria-label="Faded photo of a child playing at a playground">
      <path d="M376,0 H564 V150 C510,168 440,172 376,170 Z" fill="url(#photo-play)" opacity=".85"/>
    </g>
    <path d="M120,240 C150,232 170,226 188,222 C250,208 300,110 376,92 L376,170 C440,175 510,168 564,148 L564,436 L188,436 L188,252 C165,247 142,243 120,240 Z" fill="url(#wave-blue)"/>
    <path d="M120,240 C150,232 170,226 188,222 C250,208 300,110 376,92" fill="none" stroke="#34a6d7" stroke-width="5" opacity=".8"/>
  </svg>
  <div class="fold" style="left:188px"></div>
  <div class="fold" style="left:376px"></div>

  <h2 class="block heading-green" style="left:14px;top:222px">What<br>we do?</h2>
  <p class="block body-copy" style="left:14px;top:266px;width:162px">The Brambleway Foundation provides assistance to special needs families – in whatever way they may need it. For some families that is easing the financial burden of therapy, for others it is providing an ipad and language software so their nonverbal child can communicate. For others, it may mean providing diapers or clothing or gas cards to drive their children to doctor's appointments. We understand that each family is unique and that means assisting them in different ways, and we are here to do that.</p>
  <p class="block web" style="left:14px;top:410px">www.bramblewayfund.org</p>

  <div class="block org-name" style="left:198px;top:34px;width:168px"><span class="dot"></span>Brambleway<br>Foundation</div>
  <p class="block callout" style="left:205px;top:238px;width:165px">Do you have a special needs child?<br>You may qualify for a grant.<br>To find out:</p>
  <ul class="block steps" style="left:205px;top:318px;width:165px">
    <li>Visit www.bramblewayfund.org &amp; complete a grant inquiry form</li>
    <li>Complete the entire grant application</li>
    <li>Your application will be reviewed by the foundation &amp; you will be contacted with more information.</li>
  </ul>

  <h3 class="block difference-title" style="left:388px;top:16px">Making A Difference:</h3>
  <p class="block body-copy" style="left:388px;top:34px;width:165px;color:#2d3a4a">Below are just a few of the children we have assisted through the foundation. We assist families by:</p>
  <ul class="block difference-list" style="left:388px;top:68px">
    <li>Purchasing ipads</li>
    <li>Purchasing language software</li>
    <li>Providing gas cards</li>
    <li>Providing scholarships for therapy</li>
  </ul>
  <h2 class="block callout callout--big" style="left:392px;top:196px">How<br>can you<br>help?</h2>
  <p class="block body-copy body-copy--light" style="left:392px;top:272px;width:160px">Consider making a donation to the Brambleway Foundation. 100% of proceeds go directly to special needs families in Northern Indiana. You can write a check or visit <span class="link">www.bramblewayfund.org/donate</span> to make a donation online.</p>
</section>

<section class="sheet sheet--outside" aria-label="Brochure outside spread">
  <svg class="sheet-art" viewBox="0 0 564 436">
    <defs>
      <linearGradient id="panel-blue" x1="0" y1="0" x2="0" y2="1">
        <stop offset="0" stop-color="#0355a3"/>
        <stop offset=".6" stop-color="#3176b5"/>
        <stop offset="1" stop-color="#34a6d7"/>
      </linearGradient>
      <linearGradient id="photo-father" x1="0" y1="0" x2="1" y2="1">
        <stop offset="0" stop-color="#c9c27a"/>
        <stop offset=".55" stop-color="#2f5fa8"/>
        <stop offset="1" stop-color="#6b6a60"/>
      </linearGradient>
    </defs>
    <rect width="564" height="436" fill="url(#panel-blue)"/>
    <g role="img" aria-label="Photo of a father and his son standing against a painted wall">
      <path d="M188,0 H376 V205 C330,235 260,250 188,222 Z" fill="url(#photo-father)"/>
    </g>
    <path d="M376,0 H564 V118 C500,124 440,148 376,170 Z" fill="#fff"/>
    <path d="M376,170 C440,148 500,124 564,118 V138 C500,144 440,166 376,188 Z" fill="#9bcb3b"/>
  </svg>
  <div class="fold" style="left:188px"></div>
  <div class="fold" style="left:376px"></div>

  <h2 class="block story-title" style="left:14px;top:26px;width:160px">Our Story</h2>
  <p class="block body-copy body-copy--light" style="left:14px;top:48px;width:162px">The Brambleway Foundation was created in 2015 by my wife, Maren, and I, parents of a child with autism. As parents of a special needs child, we understand the unique emotional and financial struggles that come with raising a child who has special needs. Through our personal experience and work with Harborview Autism Center, we saw the overwhelming need in our local community for an organization to provide support to these families who were struggling. It was this recognition of the gap in services for these families that motivated us to create the Brambleway Foundation, an organization dedicated to specifically providing assistance to struggling special needs families. It is through this foundation that we hope to continue to provide hope to special needs families in Northern Indiana.</p>
  <p class="block signature" style="left:14px;top:300px;width:162px"><strong>Daniel Ashcroft</strong><br>Founder, Brambleway Foundation</p>

  <div class="block contact" style="left:200px;top:330px;width:164px">
    574-555-0182<br>www.bramblewayfund.org<br>info@bramblewayfund.org
    <hr>
    1820 Orchard Ridge Drive<br>Fairhaven, IN 46599
  </div>

  <div class="block org-name" style="left:386px;top:40px;width:168px"><span class="dot"></span>Brambleway<br>Foundation</div>
  <p class="block tagline" style="left:398px;top:220px"><span>Providing</span><span>hope</span><span>for special</span><span>needs</span><span>families</span></p>
  <p class="block web" style="left:398px;top:412px;color:#cfe6f5;font-size:7px;letter-spacing:3px">www.bramblewayfund.org</p>
</section>

</body>
</html>
```